Psychologist website

Simple psychologist website
Site map:
home
self-test
common conditions
children
contact
about
info

Current website:
http://www.corvalepsychology.com.au/

Not in love with logo, or colours etc - open brief
Happy for new font/style/logo for company name

Customer wants clean, credible and warm and friendly look & feel
stock photos OK

Brief:

One home page - simple with 2 or 3 small areas to tease and attract the user and one template page to suit all the other pages

Pages structurally similar to
http://www.wendlecourt.com.au/
In that the home page is different and the other pages are based on one template

Requirements
Must have
• 2 pages - one home page and one template page
• navigation for site map

```html
<!DOCTYPE html>
<html lang="en">
<head>
<meta charset="utf-8">
<title>Corvale &amp; Associates – Clinical Psychologists</title>
<link href="https://fonts.googleapis.com/css2?family=Montserrat:wght@500;600;700&family=Tinos&family=Roboto+Condensed&family=Varela+Round&family=Courgette&display=swap" rel="stylesheet">
<style>
:root{
  --green:#0b7a3e;
  --green-dark:#0a6a35;
  --green-text:#137a3d;
  --mint:#d9f5ea;
  --mint-head:#8ed9c0;
  --mint-box:#e6f8f0;
  --grey-bg:#f1f1f1;
  --ink:#1d1d1d;
  --cell:#d6d6d6;
}
*{box-sizing:border-box;margin:0;padding:0}
html,body{width:1141px;height:1200px;overflow:hidden}
body{position:relative;background:var(--grey-bg);font-family:"Tinos",serif;color:var(--ink)}
.top-band{position:absolute;left:0;top:0;width:1141px;height:347px;background:linear-gradient(#dcf7ec 0%,#c9e6da 40%,#9aa49f 100%)}
.sheet{position:absolute;left:129px;top:444px;width:883px;height:561px;background:linear-gradient(#e6e6e6 0,#fff 40px)}
.brand{position:absolute;left:145px;top:38px}
.brand-name{font:500 25px/1 "Montserrat",sans-serif;color:var(--green);letter-spacing:1px}
.brand-tag{margin-top:10px;font:13px/1 "Tinos",serif;letter-spacing:6.5px;color:#222}
.social{position:absolute;left:893px;top:16px;display:flex;gap:3px}
.social span{width:23px;height:21px;background:var(--green)}
.call{position:absolute;right:147px;top:61px;text-align:right;font-family:"Roboto Condensed",sans-serif;color:var(--green)}
.call-label{font-size:19px}
.call-number{font-size:40px;line-height:46px;display:flex;align-items:center;gap:6px;justify-content:flex-end}
.nav{position:absolute;left:129px;top:132px;width:883px;height:33px;background:var(--green);border-radius:3px;display:flex;align-items:center;padding-left:18px}
.nav a{font:500 12.5px "Montserrat",sans-serif;color:#fff;text-decoration:none;letter-spacing:.6px;margin-right:43px}
.hero{position:absolute;left:129px;top:173px;width:883px;height:272px;border:1px solid #3aa070;border-radius:3px;overflow:hidden;background:linear-gradient(100deg,#8fdcce 0%,#c8efe6 35%,#e9f7f3 55%,#dfe8ea 100%)}
.hero-photo{position:absolute;right:0;top:0;width:450px;height:272px;background:linear-gradient(90deg,rgba(230,240,242,0) 0%,#d8e1e4 30%,#c9cfd2 60%,#a8a09a 100%)}
.hero h1{position:absolute;left:64px;top:28px;width:410px;font:700 26px/30px "Montserrat",sans-serif;color:var(--green);letter-spacing:.5px}
.hero-arrow{position:absolute;top:118px;width:26px;height:26px;border-radius:50%;background:rgba(255,255,255,.55)}
.dots{position:absolute;left:433px;top:251px;display:flex;gap:7px}
.dots span{width:11px;height:11px;border-radius:50%;background:#fff;box-shadow:0 0 2px #777}
.dots span.on{background:radial-gradient(#222 30%,#fff 35%)}
.intro{position:absolute;left:147px;top:484px;width:850px;font-size:11.6px;line-height:14.6px}
.intro p{margin-bottom:14.6px}
.card{position:absolute;top:727px;width:259px;height:260px;border:1px solid var(--green);background:linear-gradient(#fff,var(--mint-box))}
.card-head{height:48px;background:var(--mint-head);display:flex;align-items:center;gap:8px;padding-left:12px;font:700 17.5px "Montserrat",sans-serif;letter-spacing:.8px;color:#111}
.card-body{padding:12px 14px;font-size:11.6px;line-height:14.6px}
.files{margin-top:14px;background:var(--cell)}
.file{display:flex;align-items:center;height:46px;border-bottom:1px solid #eee}
.file-icon{width:56px;height:100%;display:flex;align-items:center;justify-content:center;border-right:1px solid #888}
.file-icon span{width:40px;height:28px;border-radius:4px;background:#555}
.file-name{padding-left:8px}
.grid{margin-top:12px;display:grid;grid-template-columns:1fr 1fr 1fr;gap:2px 1px;background:#fff}
.grid div{background:var(--cell);height:33px;display:flex;align-items:center;justify-content:center;font-size:11.6px;letter-spacing:.5px}
.grid .w2{grid-column:span 2}.grid .w3{grid-column:span 3}
.more{text-align:right;margin-top:14px;font:11px "Varela Round",sans-serif;color:#d23a00}
.announce{padding:18px 20px 0 31px;font:13px/19px "Varela Round",sans-serif;color:#111}
.announce a{color:var(--green);text-decoration:none}
.footer{position:absolute;left:0;top:1005px;width:1141px;height:169px;background:var(--green);color:#fff;font-family:"Varela Round",sans-serif}
.footer h3{font:500 20px "Montserrat",sans-serif;color:#9be3bd;letter-spacing:1px}
.sitemap{position:absolute;left:144px;top:4px}
.sitemap a{display:block;color:#fff;text-decoration:none;font-size:11.5px;line-height:19px;padding-left:3px}
.slogan{position:absolute;left:388px;top:26px;font:21px/31px "Courgette",cursive;color:#fff}
.contact{position:absolute;left:750px;top:4px;font-size:11.5px}
.contact-row{display:flex;align-items:center;gap:10px;margin-top:6px}
.contact-row svg{flex:none}
.copyright{position:absolute;left:0;top:1174px;width:1141px;height:26px;background:var(--green-dark);color:#fff;text-align:center;font:9.5px/26px "Varela Round",sans-serif}
</style>
</head>
<body>
<div class="top-band"></div>
<div class="sheet"></div>

<header>
  <div class="brand">
    <div class="brand-name">CORVALE &amp; ASSOCIATES</div>
    <div class="brand-tag">CLINICAL PSYCHOLOGISTS</div>
  </div>
  <div class="social"><span></span><span></span><span></span><span></span></div>
  <div class="call">
    <div class="call-label">Call now for appointments and enquiries</div>
    <div class="call-number">
      <svg width="26" height="26" viewBox="0 0 24 24"><path d="M6.6 10.8c1.4 2.8 3.8 5.1 6.6 6.6l2.2-2.2c.3-.3.7-.4 1-.2 1.1.4 2.3.6 3.6.6.6 0 1 .4 1 1V20c0 .6-.4 1-1 1C10.6 21 3 13.4 3 4c0-.6.4-1 1-1h3.5c.6 0 1 .4 1 1 0 1.3.2 2.5.6 3.6.1.3 0 .7-.2 1z" fill="#222"/></svg>
      94552810
    </div>
  </div>
</header>

<nav class="nav">
  <a href="#">HOME</a><a href="#">SELF-TEST</a><a href="#">COMMON CONDITIONS</a><a href="#">CHILDREN</a><a href="#">CONTACT</a><a href="#">ABOUT</a><a href="#">INFO</a>
</nav>

<section class="hero">
  <div class="hero-photo" role="img" aria-label="Stock photo of a psychologist in a white coat taking notes during a session with a client"></div>
  <h1>Psychologists, in Sydney, Chatswood, and Westmead. We provide expert treatment for depression, anxiety, eating disorders and other issues.</h1>
  <div class="hero-arrow" style="left:12px"></div>
  <div class="hero-arrow" style="right:14px"></div>
  <div class="dots"><span class="on"></span><span></span><span></span><span></span></div>
</section>

<main class="intro">
  <p>Specialising in cognitive-behaviour therapy (CBT) for adults experiencing difficulties with depression, anxiety, eating disorders, stress, trauma, adjustment to illness or disability, and other common issues.</p>
  <p>We also offer therapy and assessment for children and adolescents and their families experiencing problems with anxiety, behaviour, anger, sleep, depression, ADHD and other common issues.</p>
  <p>Our psychologists provide a comfortable, supportive, and confidential environment for their clients. Our first goal is for you to feel comfortable in exploring issues and sharing sharing your concerns, knowing that you have been heard and understood. It is in this kind of environment that client and therapist can work productively to understand problems and seek solutions.</p>
  <p>We emphasise the importance of using techniques that have been demonstrated as effective by independent research. The main therapeutic technique used by our clinicians is Cognitive Behaviour Therapy (CBT).</p>
  <p>Our Psychologists are fully registered and qualified professionals. All are highly trained with Masters or Doctoral degrees in Clinical Psychology and offer a range of specialisations. All clinicians participate in ongoing professional development to keep up-to-date with the latest and most effective treatments.</p>
</main>

<section class="card" style="left:147px">
  <div class="card-head">
    <svg width="28" height="34" viewBox="0 0 28 34"><path d="M8 0h12v18h8L14 34 0 18h8z" fill="#222"/></svg>
    LATEST LECTURE
  </div>
  <div class="card-body" style="padding-top:10px">
    Handouts from the talk by Dana on managing dental phobia are available here to down load:
    <div class="files">
      <div class="file"><div class="file-icon"><span></span></div><div class="file-name">PowerPoint Presentation<br>(dental phobia lecture slides)</div></div>
      <div class="file"><div class="file-icon"><span></span></div><div class="file-name">Dental Phobia Talk/<br>Assessment Checklist.pdf</div></div>
      <div class="file" style="border:0"><div class="file-icon"><span></span></div><div class="file-name">Dental Phobia Talk/Hints for<br>patients with phobias.pdf</div></div>
    </div>
  </div>
</section>

<section class="card" style="left:441px">
  <div class="card-head" style="font-size:18px">
    <svg width="28" height="36" viewBox="0 0 28 36"><rect x="2" y="5" width="24" height="30" rx="2" fill="none" stroke="#222" stroke-width="3"/><rect x="9" y="1" width="10" height="7" fill="#222"/><path d="M5 22h5l2-5 3 9 2-4h6" fill="none" stroke="#222" stroke-width="2"/></svg>
    SERVICES&nbsp; OFFERED
  </div>
  <div class="card-body" style="padding:12px 14px 0 17px">
    Clinical psychologists, in Sydney, Chatswood, and Westmead, providing cognitive-behaviour therapy (CBT), treatment, and counselling, for depression, anxiety and other issues
    <div class="grid">
      <div>MOOD</div><div>TRAUMA</div><div>ANXIETY</div>
      <div>ADHD</div><div class="w2">EATING DISORDERS</div>
      <div class="w3">PSYCHOMETRIC ASSESSMENT</div>
    </div>
    <div class="more">Learn more ➔</div>
  </div>
</section>

<section class="card" style="left:734px">
  <div class="card-head">
    <svg width="46" height="34" viewBox="0 0 46 34"><ellipse cx="16" cy="13" rx="15" ry="11" fill="#222"/><path d="M6 22l-3 8 9-5z" fill="#222"/><ellipse cx="30" cy="18" rx="14" ry="10" fill="#222" stroke="#8ed9c0" stroke-width="2"/><path d="M36 26l4 7-9-5z" fill="#222"/></svg>
    ANNOUNCING...
  </div>
  <div class="announce">
    A new child, adolescent and family clinic as a sub-group of Corvale and Associates; KIDSMIND CLINIC. We offer specialist assessment, therapy, training for teachers, school visits.<br>
    <a href="#">www.kidsmindclinic.com.au</a>
  </div>
</section>

<footer class="footer">
  <div class="sitemap">
    <h3>Sitemap</h3>
    <a href="#">Home</a><a href="#">Our Services</a><a href="#">FAQs</a><a href="#">Our Staff</a><a href="#">Appointments</a><a href="#">Testimonials</a><a href="#">Contact Us</a>
  </div>
  <div class="slogan">Clinical psychologists, providing<br>CBT, treatment and counselling<br>throughout Sydney.</div>
  <div class="contact">
    <h3>Contact info</h3>
    <div class="contact-row" style="margin-top:0">
      <svg width="18" height="26" viewBox="0 0 18 26"><path d="M9 0a9 9 0 0 1 9 9c0 6-9 17-9 17S0 15 0 9a9 9 0 0 1 9-9z" fill="#f08a1c"/><circle cx="9" cy="9" r="3.5" fill="#fff"/></svg>
      <div style="line-height:13px">Corvale &amp; Associates<br>PO Box 712<br>Westmead NSW 2145</div>
    </div>
    <div class="contact-row" style="margin-top:12px">
      <svg width="22" height="18" viewBox="0 0 22 18"><path d="M2 6c6-6 12-6 18 0l-3 3-3-2V5H8v2L5 9z" fill="#ddd"/><rect x="5" y="9" width="12" height="8" rx="2" fill="#ddd"/></svg>
      (02) 9455 2810
    </div>
    <div class="contact-row" style="margin-top:14px">
      <svg width="22" height="22" viewBox="0 0 22 22"><rect x="6" y="1" width="10" height="8" fill="#fff"/><rect x="1" y="8" width="20" height="9" rx="2" fill="#ccc"/><rect x="5" y="14" width="12" height="7" fill="#fff"/></svg>
      (02) 9455 2811
    </div>
    <div class="contact-row" style="margin-top:12px">
      <svg width="22" height="20" viewBox="0 0 22 20"><rect x="1" y="3" width="20" height="15" fill="#e6f2da"/><path d="M1 3l10 8 10-8" fill="none" stroke="#7cb35a" stroke-width="1.5"/></svg>
      info@corvalepsychology.com.au
    </div>
  </div>
</footer>
<div class="copyright">Copyright © 2013 Corvale Associates Clinical Psychologists. All Rights Reserved.</div>
</body>
</html>
```